Design refresh of existing HR Application

Talvora is an HR & Payroll processing software, already in use by thousands of people. It is a feature packed, enterprise-grade software that is also simple and user friendly. Visit us at https://talvora.example

Seeking a refresh of the app design/UI.

Key objectives are to make it "sleeker", more professional and polished, whist still retaining functionality. Not intended to be a massive overhaul, but more of reorganization and improvements on design elements.

You may login to our demo account to see the app live.
https://app.talvora.example/login
User: demo@talvora.example
Password: Bex47

Target Market(s)

HR Managers, business administrators/owners and employees.

Industry/Entity Type

Business Software

Number of Pages Required

4 page

Font styles to use
Other font styles liked:
• Lato

Colors
0255a3
3377b5
00a990
33b8a4
f37122
faa54b

Requirements
Must have
• Must retain the current functionality on each page.
Nice to have
• Fine to suggest changes to colors, font sizes, card designs, moving sections around and any other design element changes.

```html
<!DOCTYPE html>
<html lang="en">
<head>
<meta charset="utf-8">
<title>Talvora – Dashboard</title>
<link rel="stylesheet" href="https://fonts.googleapis.com/css2?family=Nunito+Sans:wght@400;600;700&display=swap">
<style>
:root{
  --blue:#0255a3;
  --blue-mid:#3377b5;
  --green:#00a990;
  --green-soft:#1fc19b;
  --orange:#f37122;
  --amber:#faa54b;
  --yellow:#f8c21c;
  --purple:#a64ff0;
  --red:#e4505b;
  --ink:#2b2f3a;
  --muted:#8a8f9c;
  --line:#eceef3;
  --panel:#f4f5f9;
  --cell:#eef0f5;
  --white:#fff;
}
*{box-sizing:border-box;margin:0;padding:0}
html,body{width:1200px;height:1200px;overflow:hidden}
body{background:var(--white);font-family:"Nunito Sans",sans-serif;color:var(--ink);position:relative}
.brand{position:absolute;left:35px;top:44px;font-size:28px;font-weight:700;color:var(--blue)}
.greeting{position:absolute;left:162px;top:42px;font-size:29px;font-weight:400;color:var(--blue)}
.avatar{position:absolute;left:1130px;top:29px;width:34px;height:34px;border-radius:50%;background:linear-gradient(135deg,#7a5a4a,#3b3a44)}
.avatar::after{content:"";position:absolute;right:-1px;top:1px;width:7px;height:7px;border-radius:50%;background:var(--green-soft);border:1px solid #fff}

.sidenav{position:absolute;left:30px;top:170px;width:132px}
.nav-item{position:absolute;left:0;display:flex;align-items:center;gap:10px;font-size:13px;color:#a9adb8;width:132px}
.nav-item svg{width:17px;height:17px;stroke:#b5b9c3;fill:none;stroke-width:1.3}
.nav-item.active{color:var(--blue);font-weight:600;font-size:14px}
.nav-item.active svg{stroke:var(--blue)}
.nav-item.active::after{content:"";position:absolute;right:0;top:-2px;width:3px;height:15px;background:var(--blue)}

.workspace{position:absolute;left:162px;top:112px;width:1002px;height:1120px;background:var(--panel);border-radius:14px 14px 0 0}
.card{position:absolute;background:var(--white);border-radius:4px;box-shadow:0 1px 3px rgba(40,50,80,.05)}
.card-title{height:52px;padding:20px 21px 0;font-size:17px;font-weight:600;border-bottom:1px solid var(--line)}
.card-head{display:flex;justify-content:space-between;align-items:flex-start}
.star-link{display:flex;align-items:center;gap:5px;font-size:13px;color:var(--ink);font-weight:600;padding-top:2px}
.star-link svg{width:15px;height:15px;fill:none;stroke:var(--blue-mid);stroke-width:1.4}

.event{left:23px;top:29px;width:262px;height:225px}
.event .date{position:absolute;left:21px;top:75px;font-size:12px;color:var(--muted)}
.event .shift{position:absolute;left:21px;top:102px;font-size:18px;font-weight:600;color:var(--green-soft);line-height:28px}
.event .checkin{position:absolute;right:23px;top:104px;text-align:right;font-size:12px;color:var(--blue)}
.event .checkin b{display:block;font-size:18px;font-weight:600;color:var(--green-soft);margin-top:4px}
.event .branch{position:absolute;left:21px;top:185px;font-size:12.5px;color:var(--muted)}

.schedule{left:306px;top:29px;width:456px;height:225px}
.schedule .card-title{width:255px}
.shift-row{position:absolute;left:21px;width:234px;display:flex;align-items:center;font-size:11.5px;line-height:15px}
.day-badge{width:34px;height:34px;border-radius:50%;color:#fff;font-size:12px;font-weight:600;display:flex;align-items:center;justify-content:center;margin-right:10px}
.shift-date{width:29px;text-align:right;color:var(--muted);margin-right:16px}
.shift-divider{position:absolute;left:0;top:134px;width:255px;border-top:1px solid var(--line)}
.calendar{position:absolute;left:279px;top:58px;width:160px}
.cal-head{text-align:center;font-size:10px;margin-bottom:7px}
.cal-head span{color:#b5b9c3;font-size:7px;margin:0 18px}
.cal-grid{display:grid;grid-template-columns:repeat(7,19px);gap:4px;justify-content:center}
.cal-grid .dow{font-size:9px;color:#a9adb8;text-align:center;height:10px}
.cal-grid .d{height:17px;background:var(--cell);font-size:7.5px;color:#6b7080;display:flex;align-items:center;justify-content:center;border-radius:1px}
.cal-grid .d.off{color:#b8bcc6}
.cal-grid .d.we{background:var(--red);color:#fff}

.timeoff{left:784px;top:29px;width:191px;height:225px}
.leave-row{position:absolute;left:21px;right:21px;display:flex;align-items:center;font-size:11.5px;line-height:15px}
.tile{width:31px;height:31px;border-radius:3px;display:flex;align-items:center;justify-content:center;margin-right:15px;flex:none}
.tile svg{width:14px;height:14px;fill:none;stroke:#fff;stroke-width:1.5}
.leave-row .count{margin-left:auto;text-align:right}
.leave-row .count b{display:block;color:var(--green-soft);font-size:17px;font-weight:600;line-height:16px}
.row-line{position:absolute;left:0;right:0;border-top:1px solid var(--line)}
.request-btn{position:absolute;left:21px;top:176px;width:150px;height:29px;border:1px solid var(--blue);border-radius:3px;color:var(--blue);font-size:10px;display:flex;align-items:center;justify-content:center}

.tardy{left:23px;top:277px;width:310px;height:253px}
.on-leave{left:355px;top:277px;width:407px;height:253px}
.person{position:absolute;left:21px;display:flex;align-items:center;font-size:12px;line-height:15px}
.photo{width:33px;height:33px;border-radius:50%;margin-right:9px;flex:none}
.person small{display:block;font-size:10px;color:var(--muted);line-height:13px}
.person em{display:block;font-style:normal;font-weight:700;color:var(--green-soft);font-size:12px}
.filter{position:absolute;right:36px;top:17px;font-size:11.5px;color:var(--muted);display:flex;align-items:center;gap:7px}
.filter svg{width:12px;height:12px;fill:none;stroke:#a9adb8;stroke-width:1.2}
.filter-menu{position:absolute;left:297px;top:40px;width:92px;background:#fff;box-shadow:0 2px 8px rgba(40,50,80,.1);border-radius:3px;font-size:7px;color:#6b7080}
.filter-menu div{padding:0 11px;height:18px;display:flex;align-items:center}
.filter-menu .on{background:#dce8fb;color:var(--blue-mid);height:28px}

.quick{left:784px;top:277px;width:194px;height:253px}
.quick-item{position:absolute;left:21px;right:0;display:flex;align-items:center;font-size:11.5px}
.quick-item .tile{margin-right:9px}

.notices{left:23px;top:551px;width:466px;height:560px}
.announcements{left:512px;top:551px;width:466px;height:560px}
.notice{position:absolute;left:0;right:0;display:flex;align-items:center;padding:0 23px;font-size:11.5px;line-height:15px}
.notice .tile{width:33px;height:33px;margin-right:13px}
</style>
</head>
<body>

<div class="brand">Talvora</div>
<h1 class="greeting">Good afternoon Demo, it's great to see you!</h1>
<div class="avatar" role="img" aria-label="User profile photo"></div>

<nav class="sidenav">
  <div class="nav-item active" style="top:5px">
    <svg viewBox="0 0 17 17"><rect x="1" y="1" width="6" height="6" rx="1"/><rect x="10" y="1" width="6" height="6" rx="1"/><rect x="1" y="10" width="6" height="6" rx="1"/><rect x="10" y="10" width="6" height="6" rx="1"/></svg>Dashboard</div>
  <div class="nav-item" style="top:72px"><svg viewBox="0 0 17 17"><circle cx="8.5" cy="5" r="3.5"/><path d="M2 16c0-4 3-6 6.5-6s6.5 2 6.5 6z"/></svg>Employees</div>
  <div class="nav-item" style="top:132px"><svg viewBox="0 0 17 17"><rect x="1.5" y="2.5" width="14" height="13"/><path d="M1.5 6.5h14M6 6.5v9M11 6.5v9M1.5 11h14M5 1v3M12 1v3"/></svg>Calendar</div>
  <div class="nav-item" style="top:197px"><svg viewBox="0 0 17 17"><rect x="2" y="1.5" width="13" height="14"/><path d="M5 5h3M5 8.5h7M5 12h7M10 5h2"/></svg>Expenses</div>
  <div class="nav-item" style="top:264px"><svg viewBox="0 0 17 17"><rect x="2" y="3" width="10" height="13"/><path d="M5 3V1h10v12h-3M7 7v5M5.5 8.5h3M5.5 10.5h3"/></svg>Payroll</div>
  <div class="nav-item" style="top:333px"><svg viewBox="0 0 17 17"><path d="M5 1h7l-2 3h-3zM4 6h9l2 10H2z"/><path d="M8.5 8v6M7 9.5h3M7 12.5h3"/></svg>Loan</div>
  <div class="nav-item" style="top:401px"><svg viewBox="0 0 17 17"><path d="M2 1h9l4 4v11H2z"/><path d="M5 14v-3M8 14V9M11 14v-5"/></svg>Reports</div>
  <div class="nav-item" style="top:468px"><svg viewBox="0 0 17 17"><circle cx="8.5" cy="8.5" r="2.5"/><circle cx="8.5" cy="8.5" r="6.5" stroke-dasharray="3 1.5"/></svg>Settings</div>
</nav>

<main class="workspace">

  <section class="card event">
    <h2 class="card-title">Today’s Event</h2>
    <div class="date">Tue, 26 May 20</div>
    <div class="shift">09:00<br>18:00</div>
    <div class="checkin">Checked In<b>08:50</b></div>
    <div class="branch">Working Branch B</div>
  </section>

  <section class="card schedule">
    <h2 class="card-title">My Schedule</h2>
    <div class="shift-row" style="top:80px">
      <div class="day-badge" style="background:var(--green)">Tue</div>
      <div class="shift-date">May<br>26</div>
      <div>09:00 Working<br>18:00 Branch B</div>
    </div>
    <div class="shift-divider"></div>
    <div class="shift-row" style="top:156px">
      <div class="day-badge" style="background:var(--blue-mid)">Thu</div>
      <div class="shift-date">May<br>28</div>
      <div>10:00 Work (Project A)<br>12:00 Branch A</div>
    </div>
    <div class="calendar">
      <div class="cal-head"><span>◂</span>May 2020<span>▸</span></div>
      <div class="cal-grid">
        <div class="dow">S</div><div class="dow">M</div><div class="dow">T</div><div class="dow">W</div><div class="dow">T</div><div class="dow">F</div><div class="dow">S</div>
        <div class="d off">29</div><div class="d off">30</div><div class="d off">31</div><div class="d">01</div><div class="d">02</div><div class="d">03</div><div class="d we">04</div>
        <div class="d we">05</div><div class="d">06</div><div class="d">07</div><div class="d">08</div><div class="d">09</div><div class="d">10</div><div class="d we">11</div>
        <div class="d we">12</div><div class="d">13</div><div class="d">14</div><div class="d">15</div><div class="d">16</div><div class="d">17</div><div class="d we">18</div>
        <div class="d we">19</div><div class="d">20</div><div class="d">21</div><div class="d">22</div><div class="d">23</div><div class="d">24</div><div class="d we">25</div>
        <div class="d we">26</div><div class="d">27</div><div class="d">28</div><div class="d">29</div><div class="d">30</div><div class="d">31</div><div class="d we">31</div>
      </div>
    </div>
  </section>

  <section class="card timeoff">
    <h2 class="card-title">My Time off</h2>
    <div class="leave-row" style="top:70px">
      <div class="tile" style="background:var(--blue)"><svg viewBox="0 0 14 14"><path d="M7 1a4 4 0 0 0-2 7.5V11h4V8.5A4 4 0 0 0 7 1zM5.5 13h3"/></svg></div>
      <div>Anual<br>Leave</div>
      <div class="count"><b>6</b>Left</div>
    </div>
    <div class="row-line" style="top:113px"></div>
    <div class="leave-row" style="top:125px">
      <div class="tile" style="background:var(--orange)"><svg viewBox="0 0 14 14"><path d="M4 2v4a3 3 0 0 0 6 0V2M7 9v2a2 2 0 0 0 4 0"/></svg></div>
      <div>Sick<br>Days</div>
      <div class="count"><b>1</b>Taken</div>
    </div>
    <div class="request-btn">Request</div>
  </section>

  <section class="card tardy">
    <h2 class="card-title">Tardy Today</h2>
    <div class="person" style="top:76px">
      <div class="photo" role="img" aria-label="Employee photo" style="background:linear-gradient(135deg,#e9d6c6,#b79a86)"></div>
      <div>34 Employee<small>Logistic Officer</small></div>
    </div>
    <div class="row-line" style="top:122px"></div>
    <div class="person" style="top:134px">
      <div class="photo" role="img" aria-label="Employee photo" style="background:linear-gradient(135deg,#d9c3b4,#8f7a70)"></div>
      <div>65 Employee<small>Administrator</small></div>
    </div>
  </section>

  <section class="card on-leave">
    <h2 class="card-title">Who’s On Leave Today</h2>
    <div class="filter">Filter <svg viewBox="0 0 12 12"><rect x="1" y="1" width="10" height="4" rx="2"/><rect x="1" y="7" width="10" height="4" rx="2"/></svg></div>
    <div class="person" style="top:68px">
      <div class="photo" role="img" aria-label="Employee photo" style="background:linear-gradient(135deg,#f2c96a,#b98a5c)"></div>
      <div>34 Employee<small>HR Administrator</small><em>Maternity Leave</em></div>
    </div>
    <div class="row-line" style="top:122px"></div>
    <div class="person" style="top:138px">
      <div class="photo" role="img" aria-label="Employee photo" style="background:linear-gradient(135deg,#c9c4c0,#5e5450)"></div>
      <div>65 Employee<small>Designer</small><em>Maternity Leave</em></div>
    </div>
    <div class="filter-menu">
      <div class="on">Same Department</div>
      <div style="margin-top:6px">Same Branch</div>
      <div style="margin-bottom:6px">Subordinates</div>
    </div>
  </section>

  <section class="card quick">
    <h2 class="card-title">Quick Links</h2>
    <div class="quick-item" style="top:63px"><div class="tile" style="background:#33c79a"><svg viewBox="0 0 14 14"><rect x="2" y="3" width="10" height="9"/><path d="M2 6h10M5.5 6v6M8.5 6v6"/></svg></div>Event Amendments</div>
    <div class="row-line" style="top:102px"></div>
    <div class="quick-item" style="top:112px"><div class="tile" style="background:var(--blue)"><svg viewBox="0 0 14 14"><path d="M7 1a4 4 0 0 0-2 7.5V11h4V8.5A4 4 0 0 0 7 1zM5.5 13h3"/></svg></div>Leave Requests</div>
    <div class="row-line" style="top:148px"></div>
    <div class="quick-item" style="top:161px"><div class="tile" style="background:var(--yellow)"><svg viewBox="0 0 14 14"><path d="M2 12l3-8 5 5zM9 2l1 2M12 5l-2 1M11 2l-1 1"/></svg></div>Event Requests</div>
    <div class="row-line" style="top:200px"></div>
    <div class="quick-item" style="top:210px"><div class="tile" style="background:var(--purple)"><svg viewBox="0 0 14 14"><circle cx="7" cy="7" r="5.5"/><path d="M7 3.5v7M8.7 5.2C8.3 4.6 5.3 4.3 5.3 6s3.4 1 3.4 2.8S5.8 9.7 5.3 9"/></svg></div>Payrolls Pending</div>
  </section>

  <section class="card notices">
    <div class="card-title card-head"><h2 style="font-size:17px;font-weight:600">Notifications</h2>
      <div class="star-link"><svg viewBox="0 0 15 15"><path d="M7.5 1l2 4.3 4.7.5-3.5 3.2 1 4.6-4.2-2.4-4.2 2.4 1-4.6L.8 5.8l4.7-.5z"/></svg>View Starred</div></div>
    <div class="notice" style="top:69px"><div class="tile" style="background:var(--purple)"><svg viewBox="0 0 14 14"><rect x="2" y="3" width="10" height="9"/><path d="M2 6h10M5.5 6v6M8.5 6v6"/></svg></div>
      <div>Marlow, Petra has remotely checked in for<br>Working on 20/05/2020 02:07</div></div>
    <div class="row-line" style="top:128px"></div>
    <div class="notice" style="top:135px"><div class="tile" style="background:var(--amber)"><svg viewBox="0 0 14 14"><rect x="2" y="3" width="10" height="9"/><path d="M2 6h10M5.5 6v6M8.5 6v6"/></svg></div>
      <div>Marlow, Petra requests amendment on 15 Apr 2020<br>from 09:00 - 18:00.</div></div>
    <div class="row-line" style="top:194px"></div>
    <div class="notice" style="top:201px"><div class="tile" style="background:var(--green-soft)"><svg viewBox="0 0 14 14"><path d="M4 2v4a3 3 0 0 0 6 0V2M7 9v2a2 2 0 0 0 4 0"/></svg></div>
      <div>Sick Leave on 02 Jan 2020 has been approved.</div></div>
  </section>

  <section class="card announcements">
    <div class="card-title card-head"><h2 style="font-size:17px;font-weight:600">Announcements</h2>
      <div class="star-link"><svg viewBox="0 0 15 15"><path d="M7.5 1l2 4.3 4.7.5-3.5 3.2 1 4.6-4.2-2.4-4.2 2.4 1-4.6L.8 5.8l4.7-.5z"/></svg>View Starred</div></div>
    <div class="notice" style="top:69px;padding-left:15px"><div class="tile" style="background:var(--blue-mid)"><svg viewBox="0 0 14 14"><path d="M2.5 10V7a4.5 4.5 0 0 1 9 0v3M2.5 8h2v3.5h-2zM9.5 8h2v3.5h-2z"/></svg></div>
      <div>Free Friday drinks are available in the pantry on every week until the end<br>of this year. Take the opportunity to get to know more people!</div></div>
  </section>

</main>
</body>
</html>
```